Lortexa CBD oil tincture bottle product label design

I need a product label designed for a CBD hemp oil tincture bottle. The label size should be 34mm x 62mm narrow edge leading. Format wise, a high quality jpeg or pdf.

The product is a food supplement for health benefits. The colour scheme is green/gold. The logo and all of the information on the attached label needs to be included however the image, and design/layout can be changed. I do like the label that's attached Id just like others to compare.

Target Market(s)

health/supplement market

Requirements
Must have
• Green/gold theme

```html
<!DOCTYPE html>
<html lang="en">
<head>
<meta charset="utf-8">
<title>Hemp Oil 5% CBD Label</title>
<link href="https://fonts.googleapis.com/css2?family=Roboto+Slab:wght@800;900&family=Nunito:wght@300&display=swap" rel="stylesheet">
<style>
  :root {
    --page: #f2f2f2;
    --label-green: #1e4a2b;
    --label-green-deep: #173d23;
    --edge-green: #2f8a45;
    --band-yellow: #f4e825;
    --ink-green: #1d3f26;
    --figure-light: #3f8a5c;
    --figure-dark: #1e4a2b;
    --white: #ffffff;
  }
  html, body {
    margin: 0;
    width: 1184px;
    height: 1200px;
    overflow: hidden;
    background: var(--page);
  }
  .label {
    position: absolute;
    left: 240px;
    top: 145px;
    width: 704px;
    height: 910px;
    background: var(--label-green);
    border-left: 14px solid var(--edge-green);
    border-right: 14px solid var(--edge-green);
    box-sizing: border-box;
    overflow: hidden;
    font-family: "Roboto Slab", Georgia, serif;
  }
  .band-top {
    position: absolute;
    left: 0; right: 0; top: 0;
    height: 120px;
    background: var(--band-yellow);
    border-radius: 0 0 40% 40% / 0 0 28px 28px;
    display: flex;
    align-items: center;
    justify-content: center;
    color: var(--ink-green);
    font-weight: 900;
    font-size: 40px;
    letter-spacing: 0.5px;
  }
  .figure-art {
    position: absolute;
    left: 66px;
    top: 140px;
    width: 544px;
    height: 530px;
    background: radial-gradient(ellipse at 50% 40%, var(--figure-light) 0%, rgba(63,138,92,0.45) 40%, var(--figure-dark) 75%);
    opacity: 0.85;
  }
  .logo-spot {
    position: absolute;
    left: 0; right: 0;
    top: 350px;
    text-align: center;
    font-family: "Nunito", Arial, sans-serif;
    font-weight: 300;
    font-size: 42px;
    color: #e4efe6;
  }
  .product-name {
    position: absolute;
    left: 0; right: 0;
    top: 560px;
    margin: 0;
    text-align: center;
    color: var(--white);
    font-weight: 900;
    font-size: 96px;
    line-height: 106px;
    letter-spacing: 1px;
  }
  .extract-pill {
    position: absolute;
    left: 36px;
    right: 36px;
    top: 782px;
    height: 106px;
    background: var(--white);
    border-radius: 53px 53px 53px 53px / 40px 53px 53px 40px;
    display: flex;
    align-items: center;
    justify-content: center;
    color: var(--ink-green);
    font-weight: 900;
    font-size: 44px;
  }
</style>
</head>
<body>
  <section class="label">
    <div class="figure-art" role="img" aria-label="Translucent green anatomical illustration of a human torso showing the spine and skeleton"></div>
    <div class="band-top">FULL SPECTRUM</div>
    <div class="logo-spot">Logo Here</div>
    <h1 class="product-name">HEMP OIL<br>5% CBD</h1>
    <div class="extract-pill">CO2 EXTRACTED</div>
  </section>
</body>
</html>
```